TRESSLY FACEBOOK DESIGN

I need new design for facebook https://www.facebook.com/tresslyitalia.
Our Businnes is Hair care , hair replacement , hair transplant . hair regrowth . i NEED MEDICAL AND PROFESSIONAL DESIGN. I NEED ALSO RESPONSIVE DESIGN

Target Market(s)

Consumers

Industry/Entity Type

MEDICAL AND COSMETICS

Colors
0054AA
0677BA
7BADD7
CADEEF
E8F1F8

Requirements
Must have
• MEDICAL
Nice to have
• RESPONSIVE DESIGN

```html
<!DOCTYPE html>
<html lang="it">
<head>
<meta charset="utf-8">
<title>Tressly – Facebook Cover</title>
<link rel="stylesheet" href="https://fonts.googleapis.com/css2?family=Montserrat:wght@400;500;700&display=swap">
<style>
  :root {
    --page-bg: #dbe7f3;
    --white: #ffffff;
    --navy: #0d4f97;
    --brand-dark: #0a4a8f;
    --sky: #29a9e0;
    --sky-soft: #7badd7;
    --skin-dark: #6b4431;
    --skin-mid: #b98a6e;
    --skin-light: #e2c2ab;
  }
  * { margin: 0; padding: 0; box-sizing: border-box; }
  html, body {
    width: 1200px;
    height: 900px;
    overflow: hidden;
    background: var(--page-bg);
  }
  .canvas {
    position: relative;
    width: 1200px;
    height: 900px;
  }
  .cover {
    position: absolute;
    left: 40px;
    top: 235px;
    width: 1120px;
    height: 429px;
    display: block;
    box-shadow: 0 10px 30px rgba(10, 60, 120, 0.18);
  }
  .brand-name {
    font-family: "Montserrat", sans-serif;
    font-weight: 700;
    fill: var(--brand-dark);
  }
  .tagline {
    font-family: "Montserrat", sans-serif;
    font-weight: 500;
    fill: var(--navy);
    letter-spacing: 0.2px;
  }
  .service-menu {
    font-family: "Montserrat", sans-serif;
    font-weight: 700;
    fill: var(--white);
    letter-spacing: 0.3px;
  }
</style>
</head>
<body>
<main class="canvas">
  <svg class="cover" viewBox="0 0 887 340" xmlns="http://www.w3.org/2000/svg" aria-label="Tressly Facebook cover">
    <defs>
      <linearGradient id="salon-tones" x1="0" y1="0" x2="1" y2="1">
        <stop offset="0" stop-color="var(--skin-dark)"/>
        <stop offset="0.45" stop-color="var(--skin-mid)"/>
        <stop offset="1" stop-color="var(--skin-dark)"/>
      </linearGradient>
      <radialGradient id="portrait-tones" cx="0.5" cy="0.4" r="0.6">
        <stop offset="0" stop-color="var(--skin-light)"/>
        <stop offset="1" stop-color="#4a2e22"/>
      </radialGradient>
    </defs>

    <rect class="cover-base" width="887" height="340" fill="var(--white)"/>

    <path class="hero-photo" role="img" aria-label="Woman receiving a scalp massage with long wet hair"
          d="M505,0 C540,90 515,180 560,250 C590,300 615,328 640,340 L887,340 L887,0 Z"
          fill="url(#salon-tones)"/>
    <path class="hero-edge" d="M505,0 C540,90 515,180 560,250 C590,300 615,328 640,340"
          fill="none" stroke="var(--sky)" stroke-width="9"/>

    <path class="swoosh-light" d="M0,198 C160,262 380,252 560,205 L640,340 L0,340 Z" fill="var(--sky)"/>
    <path class="band-dark" d="M0,238 C150,232 340,258 500,232 C560,222 600,290 640,340 L0,340 Z" fill="var(--navy)"/>

    <circle class="portrait-photo" role="img" aria-label="Portrait of a woman with long glossy brown hair"
            cx="528" cy="209" r="86" fill="url(#portrait-tones)" stroke="var(--sky)" stroke-width="5"/>

    <rect class="brand-mark" x="48" y="58" width="58" height="58" rx="6" fill="var(--sky)"/>
    <text class="brand-name" x="125" y="115" font-size="82">Tressly</text>
    <text class="tagline" x="52" y="155" font-size="19">CURA E REINTEGRAZIONE DEI CAPELLI</text>
    <path class="tagline-wave" d="M45,190 C160,166 300,202 405,166" fill="none" stroke="var(--sky)" stroke-width="3"/>

    <text class="service-menu" y="315" font-size="15">
      <tspan x="25">HAIR CARE</tspan>
      <tspan x="136">HAIR REPLACEMENT</tspan>
      <tspan x="323">HAIR TRANSPLANT</tspan>
    </text>
  </svg>
</main>
</body>
</html>
```